'Bright Ledger Hidden Keys' Book Cover

I need a professional book cover design for my new upcoming book that shows people how to get a high credit score.

Here are my two websites:

https://www.moneywordbank-lexa.info
https://moneywordbank-lexa.com/

I am looking for a clean, professional design that pops (emotional touch) and separates from the other books that are on the market. Cover aspect ratio 1:4 for Pagewisp version and 1:5 for the paperback version. Yellow or blue are good colors - but not must. See the basic examples that I provided. File delivery format PDF.

Book Title: Bright Ledger Hidden Keys
Byline: The Quick Lift And Mend Manual for Stellar Borrowing

Currently on Brindlecart pre-order:
https://www.brindlecart.example/Bright-Ledger-Hidden-Keys-Stellar-ebook/dp/Q48MPLRT71

I am the author of 36 published books on Brindlecart. My author profile is here:
brindlecart.example/author/gideonvarly

Targeted audience: People that want to improve or repair their bad credit score.

Target Market(s)

People/consumers in the US that want to improve or repair their credit score.

Industry/Entity Type

Consumer

Font styles to use
Sans Serif

Colors

Designer to choose colors to be used in the design.

Requirements
Must have
• Author name, Title, byline, and graphic element(s).
Nice to have
• - 2020 edition logo / batch

```html
<!DOCTYPE html>
<html lang="en">
<head>
<meta charset="utf-8">
<title>Bright Ledger Hidden Keys — Book Cover</title>
<link rel="stylesheet" href="https://fonts.googleapis.com/css2?family=Roboto+Condensed:wght@700;800;900&display=swap">
<style>
  :root {
    --cover-yellow: #fbcb0a;
    --pattern-blue: #0a84c8;
    --arrow-white: #ffffff;
    --ink: #0a0a0a;
    --title-white: #ffffff;
  }
  html, body {
    margin: 0;
    padding: 0;
    overflow: hidden;
    background: #ffffff;
  }
  .cover {
    position: relative;
    width: 768px;
    height: 1200px;
    background: var(--cover-yellow);
    overflow: hidden;
    font-family: "Roboto Condensed", "Arial Narrow", sans-serif;
  }
  .growth-graphic {
    position: absolute;
    inset: 0;
    width: 768px;
    height: 1200px;
  }
  .cover-text {
    position: absolute;
    inset: 0;
    text-align: center;
  }
  .author {
    position: absolute;
    top: 38px;
    left: 0;
    right: 0;
    margin: 0;
    font-size: 58px;
    font-weight: 800;
    color: var(--ink);
    letter-spacing: -0.5px;
    line-height: 1;
  }
  .title {
    position: absolute;
    top: 130px;
    left: 0;
    right: 0;
    margin: 0;
    font-size: 104px;
    font-weight: 900;
    color: var(--title-white);
    line-height: 102px;
    text-transform: uppercase;
    letter-spacing: -1px;
  }
  .title span { display: block; }
  .subtitle {
    position: absolute;
    top: 456px;
    left: 0;
    right: 0;
    margin: 0;
    font-size: 36px;
    font-weight: 800;
    color: var(--ink);
    line-height: 30px;
    text-transform: uppercase;
    letter-spacing: -0.5px;
  }
  .subtitle span { display: block; }
</style>
</head>
<body>
  <div class="cover">
    <svg class="growth-graphic" viewBox="0 0 1024 1600" preserveAspectRatio="none">
      <path class="rising-arrow" fill="var(--arrow-white)"
        d="M0 1318 Q300 1150 550 838 L615 940 L935 572 L884 550 L1024 452 L1024 600 L610 1010 L545 920 Q300 1200 0 1385 Z"/>
      <path class="money-pattern" role="img" aria-label="Blue field patterned with rows of dollar signs and smiling symbols"
        fill="var(--pattern-blue)"
        d="M0 1385 Q300 1200 545 920 L610 1010 L985 585 L1024 590 L1024 1600 L0 1600 Z"/>
    </svg>
    <div class="cover-text">
      <p class="author">Gideon Varly</p>
      <h1 class="title">
        <span>Bright Ledger</span>
        <span>Hidden</span>
        <span>Keys</span>
      </h1>
      <p class="subtitle">
        <span>The Quick</span>
        <span>Lift And Mend</span>
        <span>Manual for</span>
        <span>Stellar Borrowing</span>
      </p>
    </div>
  </div>
</body>
</html>
```